Ferncrest Dental, LLC business card project

Business card to be designed with current logo.
Dental office- please keep design of card that looks clean and professional.
Please include the following info:
Ferncrest Dental, LLC
Dr. Lorna Pettigrew
2871 Marlowe Street
Bethlehem, PA 18093
610-555-0193
ferncrestdental.office@examplemail.test
Hello everyone-
Reason: Just got back from overseas- will look at all designs and provide feedback. Thank you!
Reason: Polling my friends for the final selection-
thank you to all those that participated- so many talented designers!

```html
<!DOCTYPE html>
<html lang="en">
<head>
<meta charset="utf-8">
<title>Ferncrest Dental, LLC — Business Card</title>
<link rel="stylesheet" href="https://fonts.googleapis.com/css2?family=Questrial&display=swap">
<style>
  :root {
    --backdrop: #e9eaea;
    --card: #fbfbfa;
    --leaf: #b4cc73;
    --leaf-light: #dbe8ad;
    --ink-green: #4f7f23;
    --brand-green: #7fa83a;
    --social-square: #4c7d22;
  }
  * { margin: 0; padding: 0; box-sizing: border-box; }
  html, body {
    width: 1198px;
    height: 1200px;
    overflow: hidden;
    background: var(--backdrop);
  }
  .canvas {
    position: relative;
    width: 1198px;
    height: 1200px;
  }
  .card {
    position: absolute;
    left: 99px;
    top: 314px;
    width: 1000px;
    height: 572px;
    background: var(--card);
    box-shadow: 0 4px 18px rgba(0,0,0,0.12);
    overflow: hidden;
    font-family: "Questrial", sans-serif;
    font-weight: 400;
    color: var(--ink-green);
  }
  .brand {
    position: absolute;
    left: 66px;
    top: 62px;
    display: flex;
    align-items: center;
    gap: 16px;
  }
  .brand-square {
    width: 34px;
    height: 34px;
    background: var(--brand-green);
  }
  .brand-name {
    font-size: 44px;
    color: var(--brand-green);
    letter-spacing: -0.5px;
  }
  .doctor {
    position: absolute;
    left: 70px;
    top: 176px;
    font-size: 34px;
    font-weight: 400;
    color: var(--ink-green);
  }
  .contact {
    position: absolute;
    left: 72px;
    top: 372px;
    font-size: 23px;
    line-height: 1.35;
    color: var(--ink-green);
    list-style: none;
  }
  .contact .gap { margin-top: 10px; }
  .illustration {
    position: absolute;
    left: 560px;
    top: 300px;
    width: 440px;
    height: 272px;
    background: linear-gradient(160deg, var(--leaf-light) 0%, var(--leaf) 100%);
  }
  .social {
    position: absolute;
    left: 760px;
    top: 190px;
    list-style: none;
    font-size: 20px;
    color: var(--ink-green);
  }
  .social li {
    display: flex;
    align-items: center;
    gap: 12px;
    margin-bottom: 8px;
  }
  .social-square {
    width: 22px;
    height: 22px;
    background: var(--social-square);
  }
</style>
</head>
<body>
<main class="canvas">
  <article class="card">
    <div class="brand">
      <span class="brand-square"></span>
      <span class="brand-name">Ferncrest Dental, LLC</span>
    </div>

    <h1 class="doctor">Dr. Lorna Pettigrew</h1>

    <ul class="contact">
      <li>2871 Marlowe Street</li>
      <li>Bethlehem, PA 18093</li>
      <li class="gap">610-555-0193</li>
      <li>ferncrestdental.office@examplemail.test</li>
    </ul>

    <div class="illustration" role="img" aria-label="Illustration area: stylised green trees standing on a curved green hill"></div>

    <ul class="social">
      <li><span class="social-square"></span>FerncrestDental.999</li>
      <li><span class="social-square"></span>@FerncrestDental</li>
    </ul>
  </article>
</main>
</body>
</html>
```